Webdesign for silver path

"Der Sternenpfad" is a new info product that will be selled through the website maybe you will create for us.

Translated from german to english the project is named "the silver path". It´s an online video course that teaches people how to live a fulfilling, happy and healthy life.

Design paramaters
We want a serious design that embodies the real feeling of beeing happy and fulfilled. Visitors should even feel good/better when they see the website.
In color psychology some sort of calming deep green like a four-leaf clover is recommend.
Mainly the website will be the external sales page with a big video as the central attention.
We also need a member area for customers to watch our video course.

So mainly we need a eye-cathing, calming header, the content body with mainly video and just a few written words...and of course a footer for links like imprint, affiliate program etc.

What we not want:
- some kind of these exaggerated smiling photos
- that bathetic luck symbols like money or boats
Updates

Hi,

i posted a message to the design discussion. Thank you!

Industry/Entity Type

Affiliate

```html
<!DOCTYPE html>
<html lang="en">
<head>
<meta charset="utf-8">
<title>the silver path</title>
<link rel="stylesheet" href="https://fonts.googleapis.com/css2?family=Quicksand:wght@500;600;700&family=Arimo:wght@400;700&display=swap">
<style>
:root{
  --green:#0aa70a;
  --green-light:#19c619;
  --green-dark:#078b07;
  --ink:#444444;
  --ink-soft:#555555;
  --page:#f3f3f2;
  --footer:#e9e9e9;
  --rule:#b9b9b9;
  --white:#ffffff;
}
*{margin:0;padding:0;box-sizing:border-box}
html,body{width:1200px;height:709px;overflow:hidden}
body{background:var(--page);font-family:"Quicksand",sans-serif;color:var(--ink);position:relative}
.header-band{position:absolute;left:440px;top:29px;width:760px;height:35px;background:linear-gradient(var(--green-light),var(--green))}
.logo-tab{position:absolute;left:0;top:14px;width:460px;height:65px;border-radius:0 14px 14px 0;background:linear-gradient(var(--green-light),var(--green));box-shadow:0 2px 3px rgba(0,0,0,.18)}
.logo-name{position:absolute;left:90px;top:8px;font-size:39px;font-weight:700;color:var(--white);letter-spacing:.3px}
.main-nav{position:absolute;top:29px;left:660px;height:35px;display:flex;align-items:center}
.main-nav a{color:var(--white);text-decoration:none;font-size:17px;font-weight:600;padding:0 11px;border-left:1px solid rgba(255,255,255,.35);line-height:26px}
.main-nav a:first-child{border-left:none}
.hero-title{position:absolute;left:76px;top:128px;font-size:37px;font-weight:500;line-height:38px;color:var(--ink)}
.hero-title strong{color:var(--green);font-weight:700}
.benefits{position:absolute;left:76px;top:225px;list-style:none;font-size:15px;line-height:22px;color:var(--ink-soft);font-weight:500}
.btn{position:absolute;display:flex;align-items:center;justify-content:center;font-size:16px;font-weight:600;border-radius:6px}
.btn-secondary{left:94px;top:341px;width:113px;height:37px;background:linear-gradient(#ffffff,#e6e6e6);color:var(--ink);box-shadow:0 2px 3px rgba(0,0,0,.25)}
.btn-primary{left:220px;top:342px;width:93px;height:35px;background:linear-gradient(var(--green-light),var(--green-dark));color:var(--white);box-shadow:0 2px 3px rgba(0,0,0,.25)}
.video-frame{position:absolute;left:532px;top:117px;width:561px;height:351px;background:var(--white);border:1px solid #dcdcdc}
.video-still{position:absolute;left:7px;top:7px;width:546px;height:309px;background:linear-gradient(135deg,#c9d3cf 0%,#8d8170 35%,#5a4a3d 65%,#2f9a9e 100%)}
.play-overlay{position:absolute;left:214px;top:126px;width:120px;height:63px;background:rgba(30,30,30,.8)}
.video-controls{position:absolute;left:7px;top:316px;width:546px;height:30px;background:linear-gradient(#3a3a3a,#151515)}
.video-controls .time{position:absolute;top:8px;font-family:"Arimo",sans-serif;font-size:11px;color:var(--white)}
.newsletter{position:absolute;left:76px;top:502px;width:1037px;height:66px;border-radius:6px;background:linear-gradient(#ffffff,#e4e4e4);border:1px solid #e2e2e2}
.newsletter-text{position:absolute;left:22px;top:22px;font-size:16px;font-weight:500;color:var(--ink);letter-spacing:.3px}
.newsletter-input{position:absolute;left:676px;top:13px;width:243px;height:40px;background:var(--white);border:1px solid #d6d6d6;border-radius:5px}
.btn-signup{left:933px;top:15px;width:93px;height:36px;font-size:19px;background:linear-gradient(var(--green-light),var(--green-dark));color:var(--white)}
.site-footer{position:absolute;left:0;top:619px;width:1200px;height:90px;background:var(--footer);font-family:"Arimo",sans-serif}
.footer-service{position:absolute;left:94px;top:9px;font-size:13px;color:var(--ink-soft)}
.footer-links{position:absolute;right:93px;top:9px;display:flex;gap:28px;font-size:13px;font-weight:700;color:var(--ink)}
.footer-rule{position:absolute;left:94px;top:31px;width:1013px;height:1px;background:var(--rule)}
.footer-legal{position:absolute;left:94px;top:42px;font-size:13px;color:var(--ink-soft)}
.social{position:absolute;top:54px;width:26px;height:26px;border-radius:5px}
</style>
</head>
<body>
<header>
  <div class="header-band"></div>
  <div class="logo-tab"><span class="logo-name">the silver path</span></div>
  <nav class="main-nav">
    <a href="#">Home</a><a href="#">About Us</a><a href="#">Services</a><a href="#">Courses</a><a href="#">Contact Us</a>
  </nav>
</header>

<main>
  <h1 class="hero-title">Online software traning<br>videos that <strong>really</strong> work.</h1>
  <ul class="benefits">
    <li>› Learn new software, creative, and business skills.</li>
    <li>› Get on-demand access to our entire video tutorial library.</li>
    <li>› Learn at your own pace, when and where you want.</li>
    <li>› New courses added weekly at no additional cost.</li>
  </ul>
  <a class="btn btn-secondary">Learn More</a>
  <a class="btn btn-primary">Buy Now</a>

  <div class="video-frame">
    <div class="video-still" role="img" aria-label="Course video still: a group of people talking around a table in a bright classroom"></div>
    <div class="video-still" style="background:none">
      <div class="play-overlay">
        <svg width="120" height="63" viewBox="0 0 120 63"><polygon points="46,13 46,50 79,31.5" fill="#e8e8e8"/></svg>
      </div>
    </div>
    <div class="video-controls">
      <svg width="546" height="30" viewBox="0 0 546 30">
        <polygon points="11,8 11,22 23,15" fill="#7ad13a"/>
        <line x1="33" y1="0" x2="33" y2="30" stroke="#555"/>
        <rect x="72" y="0" width="288" height="30" fill="#111"/>
        <line x1="400" y1="0" x2="400" y2="30" stroke="#555"/>
        <rect x="405" y="7" width="25" height="15" rx="3" fill="none" stroke="#7ad13a" stroke-width="2"/>
        <rect x="409" y="10" width="17" height="9" fill="#7ad13a"/>
        <line x1="436" y1="0" x2="436" y2="30" stroke="#555"/>
        <polygon points="443,12 447,12 451,8 451,22 447,18 443,18" fill="#7ad13a"/>
        <g fill="#7ad13a">
          <rect x="458" y="9" width="2" height="12"/><rect x="463" y="9" width="2" height="12"/><rect x="468" y="9" width="2" height="12"/><rect x="473" y="9" width="2" height="12"/><rect x="478" y="9" width="2" height="12"/><rect x="483" y="9" width="2" height="12"/><rect x="488" y="9" width="2" height="12"/><rect x="493" y="9" width="2" height="12"/><rect x="498" y="9" width="2" height="12"/>
        </g>
        <rect x="503" y="9" width="2" height="12" fill="#fff"/>
      </svg>
      <span class="time" style="left:40px">00:00</span>
      <span class="time" style="left:368px">01:40</span>
    </div>
  </div>

  <section class="newsletter">
    <p class="newsletter-text">Subscribe to our Newaletter for New Events,&nbsp; Products &amp; Special Offers</p>
    <div class="newsletter-input"></div>
    <a class="btn btn-signup">Sign up</a>
  </section>
</main>

<footer class="site-footer">
  <p class="footer-service">For Customer Service call 555-014-2290</p>
  <div class="footer-links"><span>affiliates</span><span>imprint</span><span>contact us</span></div>
  <div class="footer-rule"></div>
  <p class="footer-legal">© 2012 silver path. All rights reserved. Privacy Policy | Terms and conditions</p>
  <span class="social" style="left:864px;background:#f0962e"></span>
  <span class="social" style="left:907px;background:#5fb6cf"></span>
  <span class="social" style="left:951px;background:#3f6bad"></span>
  <span class="social" style="left:995px;background:#c9302c"></span>
  <span class="social" style="left:1039px;background:#3d87b5"></span>
  <span class="social" style="left:1082px;background:#d5443a"></span>
</footer>
</body>
</html>
```